■レイアウトの希望について
◎2カラムで、必要に応じて上ナビも入れてください。
※全体の左右を970pxで、ナビの左右サイズを300pxでお願いします。
◎写真やイラストなどのイメージ画像は、最低1点以上入れてください。(有料画像も可)
※現サイトのイラストは自由に使用ください。

■内容について
◎サイト名のロゴは現行のものでなく新たにご提案ください。
※フォントを使用したものでOKです。
◎ヘッダーはスマホサイズになった場合のことも考えて作成してください。
※サイト名の周りは適当にキャッチを入れていただくか、文字を○○○○の形で入れてもかまいません。
◎トップページに入れる文章はできていますが、文字数が少ないのでバランスが悪ければ○○○○の形でプラスしてください。
◎ナビに入れるタイトルはページ構成から抜き出して入れてください。
※上ナビも入れる場合は項目をご提案ください。(左右ナビと変えてもダブってもOK)
※新聞奨学金を目立たせたいので、ナビを工夫されても良いかと思われます。
◎文章とページ構成は以下からダウンロードしてください。
http://www.tq5.co.jp/hlv.zip
基本的にはお任せですが、派手な色やくすんだ色は避けてください。(バランスの良い、落ち着いた色が希望)
納品ファイルは、JPG形式 (.jpg)またはPNG形式 (.png)のいずれかひとつと、イラストレーター形式 (.ai) またはフォトショップ形式 (.psd) のいずれかひとつの、計2ファイルに変更させていただきます。
申し訳ございませんが、ご了承ください。
提案の締め切り日を2日間延ばして6月20日にしました。

第一希望の新聞奨学金ページへの誘導方法がうまく、その他のアイデアも多くいただきました。
それに加え、全体のバランスや色使いが好みだったので、決めさせていただきました。
また、修正依頼などもすぐに対応いただき、助かりました。

多くのご提案をいただき、ありがとうございました。
結局は主観的な好みで決めさせていただきましたが、迷ったご提案も数点ありました。
なお、締切日ギリギリのご提案は、修正依頼が出せないので、良いご提案も見送らせていただいたものもありました。

```html
<!DOCTYPE html>
<html lang="ja">
<head>
<meta charset="utf-8">
<title>まなびナビ</title>
<link href="https://fonts.googleapis.com/css2?family=Noto+Sans+JP:wght@400;700;900&display=swap" rel="stylesheet">
<style>
:root{
  --page:#eef1f2;
  --teal:#1b9aa6;
  --teal-dark:#0f6f7a;
  --teal-pale:#e3f3f5;
  --ink:#333d40;
  --muted:#6d7a7d;
  --line:#cfdfe2;
  --accent:#e8623a;
  --white:#ffffff;
}
*{margin:0;padding:0;box-sizing:border-box}
html,body{width:795px;height:1200px;overflow:hidden}
body{background:var(--page);font-family:"Noto Sans JP",sans-serif;color:var(--ink);font-size:9px;line-height:1.5;position:relative}
.topbar{position:absolute;left:0;top:0;width:795px;height:22px;background:var(--teal-dark)}
.site{position:absolute;left:106px;top:0;width:588px;height:1200px}
.sidebar{position:absolute;left:0;top:10px;width:160px}
.main{position:absolute;left:168px;top:22px;width:420px}
.brand{background:var(--white);height:128px;display:flex;flex-direction:column;align-items:center;justify-content:center;gap:10px}
.brand-tag{font-size:8px;color:var(--muted)}
.brand-row{display:flex;align-items:center;gap:6px}
.brand-mark{width:12px;height:12px;background:var(--teal)}
.brand-name{font-weight:700;color:var(--teal);font-size:20px;line-height:1}
.side-nav{list-style:none;background:var(--white);margin-top:8px;border:1px solid var(--line)}
.side-nav li{height:50px;border-bottom:1px solid var(--line);display:flex;align-items:center;padding:0 10px;font-size:9px;font-weight:700;justify-content:space-between}
.side-nav li:last-child{border-bottom:0}
.side-nav li::after{content:"›";color:var(--teal);font-size:14px}
.side-banner{margin-top:12px;height:130px;background:linear-gradient(160deg,#dff1f4,#9fd3da);position:relative;border:1px solid var(--line)}
.side-banner p{position:absolute;left:8px;font-weight:900;color:var(--teal-dark)}
.side-banner .sb1{top:14px;font-size:9px}
.side-banner .sb2{top:34px;font-size:18px}
.side-banner .sb3{top:72px;background:#f5d23c;color:var(--ink);font-size:11px;padding:3px 6px}
.side-label{margin-top:12px;background:var(--teal);color:var(--white);font-size:8px;padding:2px 8px}
.ad{height:226px;background:linear-gradient(180deg,#ffffff,#d6eef1);border:1px solid var(--line);padding:10px;text-align:center}
.ad-name{font-weight:700;font-size:13px}
.ad-copy{margin-top:8px;font-size:9px}
.ad-big{font-size:20px;font-weight:900;color:var(--accent)}
.hero{height:242px;background:linear-gradient(135deg,#f6fafb 0%,#dfeef1 55%,#b9d8de 100%);position:relative}
.hero-nav{position:absolute;top:0;right:0;display:flex;gap:3px}
.hero-nav span{background:var(--teal);color:var(--white);font-size:8px;padding:3px 12px}
.hero-nav span.contact{background:var(--white);color:var(--teal-dark);border:1px solid var(--teal)}
.hero-photo{position:absolute;right:10px;top:24px;width:180px;height:165px;background:linear-gradient(180deg,#c8dfe4,#8fb7c0)}
.hero-title{position:absolute;left:0;right:0;top:200px;text-align:center;font-weight:900;font-size:21px;color:var(--teal-dark)}
.hero-title em{font-style:normal;color:var(--accent)}
.lead{background:var(--white);padding:8px 16px;font-size:8.5px;line-height:1.7}
.lead strong{color:var(--accent)}
.kinds{display:flex;gap:6px;margin-top:10px}
.kind{flex:1;background:var(--white);border:1px solid var(--line);height:128px;padding:6px}
.kind h3{font-size:11px;color:var(--white);background:var(--teal);text-align:center;padding:2px}
.kind .icon{height:70px;margin-top:8px;background:linear-gradient(180deg,var(--teal-pale),#c7e6ea)}
.kind p{text-align:center;margin-top:6px;font-size:8px;color:var(--muted)}
.paper{margin-top:8px;height:86px;background:var(--white);border:2px solid var(--teal);display:flex;align-items:center;position:relative}
.paper-text{padding-left:16px}
.paper-text small{font-size:9px;color:var(--muted);display:block}
.paper-text b{font-size:20px;font-weight:900;color:var(--teal-dark)}
.paper-photo{position:absolute;right:0;top:0;width:150px;height:82px;background:linear-gradient(135deg,#e6f2f4,#a9cfd6)}
.guides{display:grid;grid-template-columns:1fr 1fr;gap:12px;margin-top:12px}
.guide{background:var(--white);border:1px solid var(--line);height:202px;position:relative}
.guide h3{background:var(--teal);color:var(--white);font-size:11px;padding:6px 10px}
.guide .g-icon{position:absolute;left:10px;top:38px;width:44px;height:44px;border-radius:50%;background:var(--teal-pale)}
.guide p{padding:8px 10px 0 62px;font-size:8px;line-height:1.7;color:var(--ink)}
.guide .more{position:absolute;left:30px;right:30px;bottom:12px;background:var(--teal);color:var(--white);text-align:center;font-size:8px;padding:4px}
.footer-links{position:absolute;left:0;top:992px;width:795px;height:28px;background:var(--teal-pale);border-top:2px solid var(--teal);font-size:8px;display:flex;align-items:center;padding-left:120px;gap:14px;color:var(--teal-dark)}
.pagetop{position:absolute;right:110px;top:-2px;width:34px;height:28px}
.bottom{position:absolute;left:120px;top:1058px;width:555px;height:56px;display:flex;gap:10px}
.bottom-ad{flex:1;background:linear-gradient(90deg,#ffffff,#dceef1);border:1px solid var(--line);display:flex;align-items:center;gap:14px;padding-left:16px}
.bottom-ad b{font-size:13px}
.bottom-ad span{font-size:16px;font-weight:900;color:var(--teal-dark)}
.bottom-list{width:140px;background:var(--white);border:1px solid var(--line);font-size:8px;padding:6px 10px;color:var(--teal-dark)}
.copyright{position:absolute;left:0;top:1160px;width:795px;text-align:center;font-size:7px;color:var(--muted)}
</style>
</head>
<body>
<div class="topbar"></div>
<div class="site">
  <aside class="sidebar">
    <div class="brand">
      <div class="brand-tag">奨学金比較情報サイト</div>
      <div class="brand-row"><span class="brand-mark"></span><span class="brand-name">まなびナビ</span></div>
    </div>
    <ul class="side-nav">
      <li>いろいろな奨学金</li>
      <li>奨学金ってなに？</li>
      <li>奨学金を借りる前の準備</li>
      <li>奨学金のメリット・デメリット</li>
      <li>借りる「奨学金」</li>
      <li>稼ぐ「奨学金」</li>
      <li>もらう「奨学金」</li>
    </ul>
    <div class="side-banner" role="img" aria-label="新聞奨学会の案内バナー、学生の写真">
      <p class="sb1">進学のための新しい選択</p>
      <p class="sb2">新聞奨学会</p>
      <p class="sb3">パンフレット請求</p>
    </div>
    <div class="side-label">スポンサーリンク</div>
    <div class="ad" role="img" aria-label="学生向け会員サービスの広告、学生と商品のイラスト">
      <div class="ad-name">Campus Prime</div>
      <div class="ad-copy">学生なら今だけ特典</div>
      <div class="ad-big">2,000円</div>
      <div class="ad-copy">ポイントプレゼント</div>
    </div>
  </aside>

  <main class="main">
    <section class="hero">
      <div class="hero-photo" role="img" aria-label="学生たちの写真"></div>
      <nav class="hero-nav"><span>奨学金とは</span><span>奨学金の種類</span><span class="contact">お問い合わせ</span></nav>
      <h1 class="hero-title"><em>「学費が高いから」</em>と進学を諦める前に</h1>
    </section>
    <p class="lead">「奨学金」とは、経済的な理由で進学が難しい学生を支える制度です。<strong>学費の心配を減らし、夢への一歩を</strong>踏み出すために、様々な奨学金の仕組みや返済方法、申し込みの流れをわかりやすくご紹介します。自分に合う奨学金を見つけましょう。</p>

    <div class="kinds">
      <div class="kind"><h3>借りる奨学金</h3><div class="icon" role="img" aria-label="お金を借りる様子のイラスト"></div><p>返済が必要な奨学金</p></div>
      <div class="kind"><h3>稼ぐ奨学金</h3><div class="icon" role="img" aria-label="配達する人のイラスト"></div><p>働きながら学ぶ奨学金</p></div>
      <div class="kind"><h3>もらう奨学金</h3><div class="icon" role="img" aria-label="受け取る様子のイラスト"></div><p>返済不要の奨学金</p></div>
    </div>

    <div class="paper">
      <div class="paper-text"><small>学業・生活費</small><b>新聞社の奨学金</b></div>
      <div class="paper-photo" role="img" aria-label="新聞奨学生の写真"></div>
    </div>

    <div class="guides">
      <div class="guide"><h3>奨学金制度のしくみ</h3><div class="g-icon" role="img" aria-label="制度のアイコン"></div><p>奨学金には給付型と貸与型があり、運営する団体によって条件や金額が異なります。まずは基本的な仕組みを理解しましょう。</p><div class="more">詳しく見る</div></div>
      <div class="guide"><h3>給付方法はご週間</h3><div class="g-icon" role="img" aria-label="給付のアイコン"></div><p>奨学金の給付は毎月の振込が一般的です。入学時の一時金や給付の時期について事前に確認しておくと安心です。</p><div class="more">詳しく見る</div></div>
      <div class="guide"><h3>奨学金返済の仕方</h3><div class="g-icon" role="img" aria-label="返済のアイコン"></div><p>貸与型の奨学金は卒業後に返済が始まります。返済期間や月々の金額、猶予制度などを確認しましょう。</p><div class="more">詳しく見る</div></div>
      <div class="guide"><h3>奨学金を受けるには？</h3><div class="g-icon" role="img" aria-label="申し込みのアイコン"></div><p>申し込みには学業成績や家計の基準があります。必要な書類と締め切りを早めに準備しておきましょう。</p><div class="more">詳しく見る</div></div>
    </div>
  </main>
</div>

<div class="footer-links">
  <span>奨学金とは</span><span>いろいろな奨学金</span><span>奨学金の種類</span><span>サイトマップ</span><span>お問い合わせ</span>
  <svg class="pagetop" viewBox="0 0 34 28" aria-hidden="true"><rect width="34" height="28" fill="#1b9aa6"/><path d="M10 17 L17 10 L24 17" fill="none" stroke="#fff" stroke-width="3"/></svg>
</div>

<div class="bottom">
  <div class="bottom-ad" role="img" aria-label="学生向け就活ストアの広告バナー"><b>Campus Prime</b><span>就活応援ストア</span></div>
  <div class="bottom-list">▸ 奨学金一覧<br>▸ ローン比較<br>▸ 学費の相談</div>
</div>

<p class="copyright">Copyright (C) まなびナビ All Rights Reserved.</p>
</body>
</html>
```